Full Page Ad

We are like looking for something modern, Rustic and unique for a full page ad that includes our logo, office locations, contact information. Please see our webpage and www.BRINKClaimsworks.com. I can send our logo as well.
Updates

Looking for something elegant but industrial, rustic and modern. Added Sunday, June 4, 2017

Industry/Entity Type

Insurance

Font styles to use
Serif

Requirements
Must have
• Contact information

```html
<!DOCTYPE html>
<html lang="en">
<head>
<meta charset="utf-8">
<title>BRINK Claimsworks – Full Page Ad</title>
<link rel="stylesheet" href="https://fonts.googleapis.com/css2?family=Tinos:wght@400;700&family=Arimo:wght@400;700&display=swap">
<style>
  :root {
    --navy: #0f2350;
    --orange: #ec5f3b;
    --white: #ffffff;
    --stage: #2a2a2a;
    --photo-warm: #b39a78;
    --photo-cool: #c9c4bd;
    --serif: "Tinos", "Times New Roman", serif;
    --sans: "Arimo", Arial, sans-serif;
  }
  * { margin: 0; padding: 0; box-sizing: border-box; }
  html, body { width: 982px; height: 1200px; overflow: hidden; background: var(--stage); }
  .ad {
    position: absolute; left: 62px; top: 0;
    width: 857px; height: 1200px;
    background: var(--white); overflow: hidden;
  }
  .ad-bands { position: absolute; inset: 0; width: 857px; height: 1200px; }
  .brand { position: absolute; left: 48px; top: 44px; }
  .brand-name {
    font-family: var(--sans); font-weight: 700; font-size: 64px;
    color: var(--navy); letter-spacing: 4px; line-height: 1;
  }
  .brand-tagline {
    font-family: var(--sans); font-size: 12.5px; color: var(--navy);
    letter-spacing: 0.3px; margin-top: 8px;
  }
  .photo-ring {
    position: absolute; left: 110px; top: 151px;
    width: 670px; height: 670px; border-radius: 50%;
    background: var(--orange);
  }
  .photo {
    position: absolute; left: 109px; top: 148px;
    width: 662px; height: 662px; border-radius: 50%;
    background: linear-gradient(160deg, var(--photo-cool) 0%, var(--photo-warm) 100%);
  }
  .contact { position: absolute; left: 274px; top: 860px; color: var(--white); }
  .contact-label { font-family: var(--serif); font-size: 29px; letter-spacing: 0.5px; }
  .contact-phone {
    font-family: var(--serif); font-size: 76px; color: var(--orange);
    line-height: 1; margin-top: 8px; margin-left: -3px;
  }
  .contact-web { font-family: var(--sans); font-size: 37px; margin-top: 14px; }
  .footer { position: absolute; left: 0; top: 1148px; width: 857px; color: var(--white); }
  .footer-item {
    position: absolute; display: flex; align-items: flex-start; gap: 9px;
    font-family: var(--serif); font-size: 16px; line-height: 1.3;
  }
  .footer-item svg { flex: none; margin-top: 2px; }
  .footer-address { left: 102px; }
  .footer-phone { left: 432px; }
  .footer-fax { left: 682px; }
</style>
</head>
<body>
<main class="ad">
  <svg class="ad-bands" viewBox="0 0 857 1200" aria-hidden="true">
    <polygon points="737,0 851,0 11,1200 0,1200 0,1043" fill="var(--orange)"/>
    <polygon points="851,0 857,0 857,1200 11,1200" fill="var(--navy)"/>
  </svg>

  <header class="brand">
    <div class="brand-name">BRINK</div>
    <div class="brand-tagline">BRINK CLAIMS ADJUSTING SERVICES</div>
  </header>

  <div class="photo-ring"></div>
  <div class="photo" role="img" aria-label="Photo: firefighter in protective gear with air tanks putting out a fire amid white smoke"></div>

  <section class="contact">
    <p class="contact-label">CONTACT US:</p>
    <p class="contact-phone">1-800-555-0148</p>
    <p class="contact-web">www.BRINKClaimsworks.com</p>
  </section>

  <footer class="footer">
    <div class="footer-item footer-address">
      <svg width="10" height="14" viewBox="0 0 10 14"><path d="M5 0a5 5 0 0 0-5 5c0 4 5 9 5 9s5-5 5-9a5 5 0 0 0-5-5zm0 7a2 2 0 1 1 0-4 2 2 0 0 1 0 4z" fill="var(--orange)"/></svg>
      <span>PO Box 218, 410 Mill Road<br>Ashford Park, NY 12000</span>
    </div>
    <div class="footer-item footer-phone">
      <svg width="16" height="13" viewBox="0 0 16 13"><path d="M1 4c0-2 3-3 7-3s7 1 7 3v1h-3V4H4v1H1zM3 6h10l2 6H1z" fill="var(--orange)"/></svg>
      <span>518-555-0192</span>
    </div>
    <div class="footer-item footer-fax">
      <svg width="16" height="12" viewBox="0 0 16 12"><rect x="0" y="4" width="16" height="8" rx="1" fill="var(--orange)"/><rect x="3" y="0" width="10" height="5" fill="var(--orange)"/></svg>
      <span>888-555-0163</span>
    </div>
  </footer>
</main>
</body>
</html>
```